Tomas Verlund,M.D. Pediatric Office
Stationery, Envelopes and Biz Card
Bright & Fun-filled
Tomas Verlund,M.D.P.C.
Board Certified Pediatrician
3916 Pellingham Rd. Suite 204
Dearborn, MI 48391
tomas@verlundo.example
www.verlundo.example
Please use my logo on top and elements derived from my logo on other parts of stationery:
Suggestions: The boy and girl on the logo could be used in a playing or happy walking position at the bottom of the letterhead above the address and phone number area
and can be used at the addressee's area on the envelope in a wlcoming happy position. (Please feel free to be totally creative. I'm open to all suggestions and innovations).Different is good!!
Elements derived from logo
Be totally free and creative. You are the expert!

```html
<!DOCTYPE html>
<html lang="en">
<head>
<meta charset="utf-8">
<title>Tomas Verlund, M.D. Pediatric Office – Stationery</title>
<link rel="stylesheet" href="https://fonts.googleapis.com/css2?family=Libre+Baskerville:wght@700&family=Nunito:wght@400;600&display=swap">
<style>
  :root{
    --bg:#eceae6;
    --paper:#ffffff;
    --navy:#1d3a78;
    --pink:#e2358f;
    --yellow:#f7c21c;
    --green:#9fd154;
    --blue:#37a6de;
    --magenta:#d24fa8;
    --purple:#a765c9;
    --grass:#7cc242;
    --ink:#555;
    --kids-a:#f5c79b;
    --kids-b:#7fb3e0;
  }
  *{box-sizing:border-box;margin:0;padding:0}
  html,body{width:1200px;height:533px;overflow:hidden;background:var(--bg)}
  .canvas{position:relative;width:1200px;height:533px;font-family:"Nunito",sans-serif}

  .brand{display:flex;align-items:center;gap:5px}
  .brand-dot{width:14px;height:14px;border-radius:50%;background:var(--pink);flex:none}
  .brand-name{font-family:"Libre Baskerville",serif;font-weight:700;color:var(--navy);font-size:8px;white-space:nowrap}
  .brand-tag{color:var(--pink);font-size:5.5px}

  /* business cards */
  .card{position:absolute;width:158px;height:96px;box-shadow:0 2px 5px rgba(0,0,0,.18);overflow:hidden}
  .card-front{background:var(--paper);padding:10px}
  .card-front .contact{position:absolute;left:10px;bottom:10px;font-size:4.5px;line-height:1.45;color:var(--ink)}
  .card-back{display:flex;align-items:center;justify-content:center}
  .card-back .brand-name{color:#fff;font-size:10px}
  .card-back .brand-dot{background:#fff}
  .back-yellow{background:var(--yellow)}
  .back-green{background:var(--green)}
  .back-blue{background:var(--blue)}
  .back-pink{background:var(--magenta)}

  /* letterhead */
  .letterhead{position:absolute;left:396px;top:101px;width:365px;height:374px;background:var(--paper);box-shadow:0 2px 6px rgba(0,0,0,.2)}
  .letterhead .brand{position:absolute;left:22px;top:16px}
  .letterhead .brand-dot{width:22px;height:22px}
  .letterhead .brand-name{font-size:10px}
  .letterhead .brand-tag{font-size:6.5px}
  .letterhead .kids{position:absolute;right:18px;bottom:12px;width:64px;height:52px;border-radius:18px 18px 4px 4px;background:linear-gradient(90deg,var(--kids-a),var(--kids-b))}
  .letterhead .contact{position:absolute;left:22px;bottom:14px;font-size:5.5px;line-height:1.5;color:var(--ink)}
  .letterhead .ground{position:absolute;left:0;right:0;bottom:0;height:6px;background:var(--grass)}

  /* envelopes */
  .envelope{position:absolute;left:792px;width:384px;height:150px;background:var(--paper);box-shadow:0 2px 5px rgba(0,0,0,.2);overflow:hidden}
  .envelope svg.flap{position:absolute;left:0;top:0;width:384px;height:80px}
  .envelope .brand{position:absolute;left:16px;top:14px}
  .envelope-front .contact{position:absolute;left:16px;bottom:14px;font-size:4.5px;color:var(--ink)}
  .envelope-front .kids{position:absolute;right:70px;bottom:10px;width:70px;height:58px;border-radius:20px 20px 4px 4px;background:linear-gradient(90deg,var(--kids-a),var(--kids-b))}
  .envelope-front .ground{position:absolute;left:0;right:0;bottom:0;height:8px;background:var(--grass)}
</style>
</head>
<body>
<main class="canvas">

  <!-- business cards -->
  <section class="card card-front" style="left:34px;top:115px">
    <div class="brand"><span class="brand-dot"></span><div><div class="brand-name">Tomas Verlund,M.D.P.C.</div><div class="brand-tag">Board Certified Pediatrician</div></div></div>
    <div class="contact">3916 Pellingham Rd. Suite 204<br>Dearborn, MI 48391<br>tomas@verlundo.example<br>www.verlundo.example</div>
  </section>
  <section class="card card-front" style="left:209px;top:115px">
    <div class="brand"><span class="brand-dot"></span><div><div class="brand-name">Tomas Verlund,M.D.P.C.</div><div class="brand-tag">Board Certified Pediatrician</div></div></div>
    <div class="contact">3916 Pellingham Rd. Suite 204<br>Dearborn, MI 48391<br>tomas@verlundo.example<br>www.verlundo.example</div>
  </section>
  <section class="card card-back back-yellow" style="left:34px;top:218px"><div class="brand"><span class="brand-dot"></span><span class="brand-name">Tomas Verlund</span></div></section>
  <section class="card card-back back-green" style="left:209px;top:218px"><div class="brand"><span class="brand-dot"></span><span class="brand-name">Tomas Verlund</span></div></section>
  <section class="card card-back back-blue" style="left:34px;top:322px"><div class="brand"><span class="brand-dot"></span><span class="brand-name">Tomas Verlund</span></div></section>
  <section class="card card-back back-pink" style="left:209px;top:322px"><div class="brand"><span class="brand-dot"></span><span class="brand-name">Tomas Verlund</span></div></section>

  <!-- letterhead -->
  <section class="letterhead">
    <div class="brand"><span class="brand-dot"></span><div><div class="brand-name">Tomas Verlund,M.D.P.C.</div><div class="brand-tag">Board Certified Pediatrician</div></div></div>
    <div class="contact">3916 Pellingham Rd. Suite 204, Dearborn, MI 48391<br>Tel: (313) 555-0148<br>Fax: (313) 555-0149<br>tomas@verlundo.example</div>
    <div class="kids" role="img" aria-label="Illustration of a happy boy and girl walking"></div>
    <div class="ground"></div>
  </section>

  <!-- envelopes -->
  <section class="envelope envelope-back" style="top:100px">
    <svg class="flap" viewBox="0 0 384 80" preserveAspectRatio="none"><path d="M0 0H384V20Q192 90 0 20Z" fill="var(--yellow)"/></svg>
  </section>
  <section class="envelope envelope-back" style="top:152px">
    <svg class="flap" viewBox="0 0 384 80" preserveAspectRatio="none"><path d="M0 0H384V20Q192 90 0 20Z" fill="var(--blue)"/></svg>
  </section>
  <section class="envelope envelope-back" style="top:204px">
    <svg class="flap" viewBox="0 0 384 80" preserveAspectRatio="none"><path d="M0 0H384V20Q192 90 0 20Z" fill="var(--magenta)"/></svg>
  </section>
  <section class="envelope envelope-back" style="top:256px">
    <svg class="flap" viewBox="0 0 384 80" preserveAspectRatio="none"><path d="M0 0H384V20Q192 90 0 20Z" fill="var(--green)"/></svg>
  </section>
  <section class="envelope envelope-front" style="top:320px">
    <div class="brand"><span class="brand-dot"></span><div><div class="brand-name">Tomas Verlund,M.D.P.C.</div><div class="brand-tag">Board Certified Pediatrician</div></div></div>
    <div class="contact">3916 Pellingham Rd. Suite 204, Dearborn, MI 48391</div>
    <div class="kids" role="img" aria-label="Illustration of a boy and girl waving a welcome"></div>
    <div class="ground"></div>
  </section>

</main>
</body>
</html>
```